Coldforge Prime manufacturing Project

We are looking at getting a brand new design for a new company that deals in selling stainless tubing and other stainless still products such as handrails, Spigots, Balustrade Fittings
Glass, Glass fittings and Aluminium Channels

We require a very clean website that deals with the following colours:

Blue to light blues
Blacks
Greys to light Greys
Whites

We are open for other ideas BUT we *DO NOT* want any pinks, greens or bright colours except for backgrounds colours we have chosen above. (It can be solid, gradient or a subtle pattern)

YOU MUST KEEP THE LOGO AS IS. PLEASE DO NOT ALTER THE LOGO IN *ANY WAY* and the logo MUST be the same colours and fonts.

Logo is attached.

The site must contain these aspects:
jQuery Slider (Image slide show)
Top drop down Menus
Be no more than 900px wide
Text is to be to the w3C standards. (no special fonts)

We will chop up the design into html format. You just need to provide the PSD file.

The clients opposition is:
www.quorvatrim.example

Industry/Entity Type

It Company

Requirements
Nice to have
• Alter the logo in anyway

Files

```html
<!DOCTYPE html>
<html lang="en">
<head>
<meta charset="utf-8">
<title>Coldforge Prime Manufacturing</title>
<link href="https://fonts.googleapis.com/css2?family=Open+Sans:wght@400;600&family=Tinos&display=swap" rel="stylesheet">
<style>
:root{
  --page-black:#000;
  --white:#fff;
  --nav-grey:#555;
  --accent-blue:#3a7fc4;
  --tile-dark:#262626;
  --tile-mid:#444;
  --tile-light:#676767;
  --welcome:#535353;
  --footer:#212121;
  --menu-bg:rgba(38,38,38,.93);
}
*{margin:0;padding:0;box-sizing:border-box}
html,body{width:995px;height:1200px;overflow:hidden;background:var(--page-black)}
.stage{position:absolute;left:0;top:0;width:1200px;height:1447px;transform:scale(.829167);transform-origin:0 0;
  font-family:"Open Sans",Arial,sans-serif;
  background:
    radial-gradient(circle at 3px 3px,#3a3a3a 1.3px,transparent 1.6px) 0 0/8px 8px,
    linear-gradient(90deg,#0c0c0c,#2a2a2a 50%,#0c0c0c);
}
.stage::after{content:"";position:absolute;left:0;right:0;top:840px;bottom:0;background:linear-gradient(#0000,#000 60px)}
.sheet{position:absolute;left:139px;top:0;width:922px;height:1405px;background:var(--white);z-index:1}
.abs{position:absolute}
.top-contact{left:18px;top:15px;font-size:10.5px;color:#666;letter-spacing:.3px}
.top-contact span{margin-left:14px}
.rule{height:1px;background:#bbb}
.search{left:773px;top:11px;width:123px;height:21px;border:1px solid #aaa;font-size:12px;color:#666;padding:2px 10px}
.search svg{position:absolute;right:5px;top:3px}
.brand{left:0;width:922px;text-align:center;top:6px}
.brand-mark{width:100px;height:100px;border-radius:50%;margin:0 auto;background:radial-gradient(circle at 50% 40%,#5c7fa8,#1d2f46 70%,#0c0c0c);border:4px solid #ddd}
.brand-name{font-family:Tinos,"Times New Roman",serif;font-size:19px;color:#111;margin-top:4px;line-height:22px}
.brand-sub{font-family:Tinos,"Times New Roman",serif;font-size:8.5px;letter-spacing:2.3px;color:#111}
.nav a{position:absolute;top:119px;font-size:14px;color:var(--nav-grey);text-decoration:none;letter-spacing:.3px}
.nav a.active{color:var(--accent-blue);text-decoration:underline}
.nav-bar{left:11px;top:150px;width:900px;height:7px;background:linear-gradient(#eee,#cfcfcf)}
.pointer{left:624px;top:143px}
.hero{left:11px;top:157px;width:900px;height:336px;background:#111}
.hero div{position:absolute;top:0;height:336px}
.dropdown{left:454px;top:157px;width:393px;height:98px;background:var(--menu-bg);z-index:2}
.dropdown ul{list-style:none;position:absolute;top:14px;font-size:13px;color:var(--white);line-height:24px}
.dropdown li.current{text-decoration:underline}
.drop-thumb{position:absolute;left:304px;top:10px;width:78px;height:77px;background:var(--white);padding:6px}
.drop-thumb div{width:100%;height:100%;background:linear-gradient(160deg,#fff 20%,#c9c9c9 50%,#8c8c8c 70%,#fff 85%)}
.hero-edge{left:11px;top:494px;width:900px;height:4px;background:#ddd}
.welcome{left:11px;top:504px;width:360px;height:250px;background:var(--welcome);color:var(--white);padding:15px 22px 0 18px}
.welcome h1{font-weight:400;font-size:19px;line-height:21.5px;letter-spacing:.4px;text-align:justify}
.welcome p{font-size:12px;line-height:14.5px;margin-top:14px;text-align:justify}
.readmore{position:absolute;left:260px;top:210px;width:79px;height:25px;background:var(--white);color:#333;font-size:10px;letter-spacing:.8px;text-align:center;line-height:25px}
.tile{width:180px;height:250px}
.tile-head{height:88px;color:var(--white);padding:17px 14px 0;position:relative}
.tile-head h2{font-weight:400;font-size:15.5px;line-height:18px;letter-spacing:.3px}
.tile-head p{font-size:11px;margin-top:7px;letter-spacing:.5px}
.tile-head::after{content:"";position:absolute;left:86px;bottom:-11px;border:7px solid transparent;border-top-color:inherit;border-top-width:11px;z-index:1}
.dark{background:var(--tile-dark);border-color:var(--tile-dark)}
.mid{background:var(--tile-mid);border-color:var(--tile-mid)}
.light{background:var(--tile-light);border-color:var(--tile-light)}
.tile-photo{height:162px}
.photo-rail{background:linear-gradient(90deg,#6f6c6a 0%,#9a9794 30%,#dcdcdc 55%,#f0f0f0 80%,#5a5a5a 100%)}
.photo-bend{background:linear-gradient(180deg,#cfcfcf 0%,#9c9c9c 30%,#4a4a4a 65%,#0e0e0e 100%)}
.photo-tube{background:linear-gradient(90deg,#1a1a1a 0%,#262626 45%,#8e8e8e 65%,#c9c9c9 85%,#9a9a9a 100%)}
.lower{left:0;top:1003px;width:922px;height:332px;background:repeating-linear-gradient(160deg,#d2d2d2 0 2px,#c8c8c8 2px 4px)}
.lower h3{position:absolute;left:24px;top:33px;font-weight:400;font-size:18px;color:#333;letter-spacing:.5px}
.lower .line{position:absolute;left:11px;top:57px;width:900px;height:2px;background:#666}
.lower .copy{position:absolute;left:22px;top:83px;width:520px;font-size:11.2px;line-height:13px;color:#222}
.lower .copy p+p{margin-top:13px}
.feature-shot{position:absolute;left:587px;top:80px;width:295px;height:193px;border:1px solid #bbb;background:linear-gradient(90deg,#d8d8d8,#f4f4f4 30%,#bdbdbd 55%,#ededed 80%,#d0d0d0)}
.feature-shadow{position:absolute;left:590px;top:280px;width:290px;height:14px;background:radial-gradient(ellipse,rgba(0,0,0,.3),transparent 70%)}
.footer{left:0;top:1337px;width:922px;height:68px;background:var(--footer);color:var(--white)}
.footer .copyright{position:absolute;left:21px;top:21px;font-size:10px;font-weight:600}
.footer .contact-block{position:absolute;right:23px;top:21px;display:flex;align-items:flex-start;gap:8px}
.footer .icons{flex:none;margin-top:2px}
.footer .contact{font-size:10px;font-weight:600;text-align:right;line-height:12px}
</style>
</head>
<body>
<div class="stage">
<div class="sheet">
  <div class="abs top-contact">DESIGN@COLDFORGEPRIME.EXAMPLE <span>T: 2043 5550 0142</span></div>
  <div class="abs rule" style="left:18px;top:37px;width:380px"></div>
  <div class="abs rule" style="left:529px;top:37px;width:380px"></div>
  <div class="abs search">SEARCH
    <svg width="14" height="14" viewBox="0 0 14 14"><circle cx="8" cy="6" r="4.5" fill="none" stroke="#666" stroke-width="1.3"/><line x1="5" y1="9" x2="1" y2="13" stroke="#666" stroke-width="1.5"/></svg>
  </div>
  <div class="abs brand">
    <div class="brand-mark"></div>
    <div class="brand-name">Coldforge Prime</div>
    <div class="brand-sub">Manufacturing Co. Ltd</div>
  </div>
  <nav class="nav">
    <a style="left:27px">HOME</a>
    <a style="left:163px">ABOUT</a>
    <a style="left:276px">SERVICES</a>
    <a class="active" style="left:589px">PRODUCTS</a>
    <a style="left:701px">DOWNLOAD</a>
    <a style="left:821px">CONTACT</a>
  </nav>
  <div class="abs nav-bar"></div>
  <svg class="abs pointer" width="14" height="10"><polygon points="0,10 7,0 14,10" fill="#ccc"/></svg>

  <div class="abs hero">
    <div role="img" aria-label="Rolled stainless steel tube bracket on a concrete surface" style="left:0;width:632px;background:linear-gradient(170deg,#9a9a9a 0%,#8c8c8c 35%,#b9b9b9 60%,#a3a3a3 80%,#c4c4c4 100%)"></div>
    <div role="img" aria-label="Close-up of a flat steel bar" style="left:633px;width:87px;background:linear-gradient(180deg,#9a9a9a 0%,#c8c8c8 40%,#3a3a3a 60%,#8e8e8e 100%)"></div>
    <div role="img" aria-label="Polished stainless fitting" style="left:722px;width:86px;background:linear-gradient(180deg,#1c1c1c 0%,#6a6a6a 35%,#e8e8e8 50%,#5a5a5a 75%,#9a9a9a 100%)"></div>
    <div role="img" aria-label="Stainless glass spigot detail" style="left:810px;width:88px;background:linear-gradient(90deg,#9c9c9c,#d6d6d6 50%,#8a8a8a)"></div>
  </div>
  <div class="abs dropdown">
    <ul style="left:16px">
      <li class="current">railing system</li><li>glass system</li><li>post &amp; balustrade</li>
    </ul>
    <ul style="left:150px">
      <li>accessories</li><li>square tube fittings</li><li>sliding door &amp; canopy</li>
    </ul>
    <div class="drop-thumb" role="img" aria-label="Aluminium glass channel"><div></div></div>
  </div>
  <div class="abs hero-edge"></div>

  <div class="abs welcome">
    <h1>Welcome to Coldforge Prime, your professional supplier for railing systems, handrail fittings and glass glazing systems.</h1>
    <p>Coldforge Prime is always innovating to satisfy our customers by supplying solution of customer´s inquiry, supply a modular Railing system which is easy to use and competitively priced, develop, and design according to customer´s idea, supply Stainless Steel products</p>
    <div class="readmore">READMORE</div>
  </div>

  <div class="abs tile" style="left:371px;top:504px"><div class="tile-head dark"><h2>HAND RAIL<br>TUBE BRACKET</h2><p>2”, 3”, 1.5’</p></div><div class="tile-photo photo-rail" role="img" aria-label="Steel handrail bracket"></div></div>
  <div class="abs tile" style="left:551px;top:504px"><div class="tile-head mid"><h2>FEATURE<br>PRODUCTS</h2><p>2”, 3”, 1.5’</p></div><div class="tile-photo photo-bend" role="img" aria-label="Bent steel bar fitting"></div></div>
  <div class="abs tile" style="left:731px;top:504px"><div class="tile-head light"><h2>HAND RAIL<br>TUBE BRACKET</h2><p>2”, 3”, 1.5’</p></div><div class="tile-photo photo-tube" role="img" aria-label="Stainless tube end"></div></div>

  <div class="abs tile" style="left:11px;top:754px"><div class="tile-head dark"><h2>HAND RAIL<br>TUBE BRACKET</h2><p>2”, 3”, 1.5’</p></div><div class="tile-photo photo-rail" role="img" aria-label="Steel handrail bracket"></div></div>
  <div class="abs tile" style="left:191px;top:754px"><div class="tile-head mid"><h2>FEATURE<br>PRODUCTS</h2><p>2”, 3”, 1.5’</p></div><div class="tile-photo photo-bend" role="img" aria-label="Bent steel bar fitting"></div></div>
  <div class="abs tile" style="left:371px;top:754px"><div class="tile-head light"><h2>HAND RAIL<br>TUBE BRACKET</h2><p>2”, 3”, 1.5’</p></div><div class="tile-photo photo-tube" role="img" aria-label="Stainless tube end"></div></div>
  <div class="abs tile" style="left:551px;top:754px"><div class="tile-head mid"><h2>FEATURE<br>PRODUCTS</h2><p>2”, 3”, 1.5’</p></div><div class="tile-photo photo-bend" role="img" aria-label="Bent steel bar fitting"></div></div>
  <div class="abs tile" style="left:731px;top:754px"><div class="tile-head light"><h2>HAND RAIL<br>TUBE BRACKET</h2><p>2”, 3”, 1.5’</p></div><div class="tile-photo photo-tube" role="img" aria-label="Stainless tube end"></div></div>

  <section class="abs lower">
    <h3>TITLE HERE</h3>
    <div class="line"></div>
    <div class="copy">
      <p>Lorem ipsum dolor sit amet, consectetuer adipiscing elit, sed diam nonummy nibh euismod tincidunt ut laoreet dolore magna aliquam erat volutpat. Ut wisi enim ad minim veniam, quis nostrud exerci tation ullamcorper suscipit lobortis nisl ut aliquip ex ea commodo consequat. Duis autem vel eum iriure dolor in hendrerit in vulputate velit esse molestie consequat, vel illum dolore eu feugiat nulla facilisis at vero eros et accumsan et iusto odio dignissim qui blandit praesent luptatum zzril delenit augue duis dolore te feugait nulla facilisi.</p>
      <p>Lorem ipsum dolor sit amet, consectetuer adipiscing elit, sed diam nonummy nibh euismod tincidunt ut laoreet dolore magna aliquam erat volutpat. Ut wisi enim ad minim veniam, quis nostrud exerci tation ullamcorper suscipit lobortis nisl ut aliquip ex ea commodo consequat. Duis autem vel eum iriure dolor in hendrerit in vulputate velit esse molestie consequat, vel illum dolore eu feugiat nulla facilisis at vero eros et accumsan et iusto odio dignissim qui blandit praesent luptatum zzril delenit augue duis dolore te feugait nulla facilisi.</p>
    </div>
    <div class="feature-shot" role="img" aria-label="Stainless steel tube clamp fitting"></div>
    <div class="feature-shadow"></div>
  </section>

  <footer class="abs footer">
    <div class="copyright">Copyright © Coldforge Prime. All Rights Reserved.</div>
    <div class="contact-block">
      <svg class="icons" width="43" height="19"><rect x=".5" y=".5" width="18" height="18" rx="3" fill="none" stroke="#fff"/><rect x="23.5" y=".5" width="18" height="18" rx="3" fill="none" stroke="#fff"/></svg>
      <div class="contact">design@coldforgeprime.example<br>t: 2043 5550 0142</div>
    </div>
  </footer>
</div>
</div>
</body>
</html>
```